Flyer für Vermieter von Monteursunterkünften
Zielgruppe
Guten Tag,
wir sind eine Fima, die Monteursunterkünfte vermietet. Wir vermieten möblierte Wohnungen auf Zeit. Man kann diese buchen ab 5 Tagen bis hin zu mehreren Monaten. Sie sind für Monteure, Handwerker oder Zeitarbeiter geeignet. Die Website dient lediglich zur Inspiration für Design und Farben. Auf der Website sprechen wir eine andere Zielgruppe an.
Mit den Flyern möchten wir Handwerksbetriebe oder auch Handwerker direkt ansprechen, welche auf der Suche nach einer günstigen und möblierten Unterkunft auf Zeit sind.
Es sollen beide Logos von der QT Dwelling und der RuhOrt17 verwendet werden.
Aufgabenstellung
Sie sind auf der Suche nach einer günstigen und komfortablen Unterkunft für Ihre Mitarbeiter? Dann sind Sie bei uns genau richtig!
BUCHEN Sie JETZT SCHNELL und EINFACH: 01629 581706
• Moderne und komfortable Wohnungen
• TV und Kühlschränke auf jedem Zimmer
• Voll ausgestattete Küche
• Immer mit Balkon oder Terrasse
• Kostenloses schnelles W-Lan
• Gute Parkmöglichkeiten
• Willkommenspaket
Überzeugen Sie sich selbst von unserem Angebot und buchen Sie noch heute eines unserer Monteurzimmer! Wir freuen uns auf Ihren Besuch.

```html
<!DOCTYPE html>
<html lang="de">
<head>
<meta charset="utf-8">
<title>Flyer Monteurzimmer – QT Dwelling</title>
<link href="https://fonts.googleapis.com/css2?family=Inter:wght@400;600;700;800&display=swap" rel="stylesheet">
<style>
  :root {
    --red: #e30613;
    --ink: #111111;
    --paper: #ffffff;
    --canvas: #ffffff;
    --footer: #000000;
    --photo-warm-a: #f3e4cf;
    --photo-warm-b: #d98a5a;
    --photo-room-a: #e9e7e3;
    --photo-room-b: #b9b2a6;
  }
  * { box-sizing: border-box; margin: 0; padding: 0; }
  html, body { width: 1200px; height: 1122px; overflow: hidden; background: var(--canvas); }
  body { position: relative; font-family: "Inter", Arial, sans-serif; color: var(--ink); }

  .flyer {
    position: absolute; top: 55px; width: 504px; height: 1007px;
    background: var(--paper); overflow: hidden;
  }
  .flyer--front { left: 66px; }
  .flyer--back { left: 619px; }

  .photo { position: absolute; left: 0; top: 0; width: 100%; }
  .flyer--front .photo { height: 540px; background: linear-gradient(135deg, var(--photo-warm-a) 0%, #e9c9a6 45%, var(--photo-warm-b) 100%); }
  .flyer--back .photo { height: 345px; background: linear-gradient(180deg, var(--photo-room-a) 0%, #dcd8d1 60%, var(--photo-room-b) 100%); }

  .wave { position: absolute; left: 0; width: 504px; height: 60px; }
  .flyer--front .wave { top: 492px; }
  .flyer--back .wave { top: 300px; }

  .headline {
    position: absolute; left: 0; right: 0; top: 546px;
    text-align: center; font-weight: 700; font-size: 32px; line-height: 42px;
  }
  .accent { color: var(--red); }
  .lead {
    position: absolute; left: 0; right: 0; top: 640px;
    text-align: center; font-size: 17.5px; line-height: 27px;
  }

  .cta {
    position: absolute; left: 41px; width: 420px; height: 78px;
    background: var(--red); color: #fff; border-radius: 8px;
    transform: rotate(-1.8deg);
    display: flex; align-items: center; justify-content: center;
    text-align: center; font-weight: 800; font-size: 19px; line-height: 26px;
  }
  .flyer--front .cta { top: 748px; }
  .flyer--back .cta { top: 690px; }

  .brands {
    position: absolute; left: 0; right: 0;
    display: flex; justify-content: center; align-items: center; gap: 62px;
  }
  .flyer--front .brands { top: 868px; }
  .flyer--back .brands { top: 818px; }
  .brand { display: flex; align-items: center; gap: 8px; font-weight: 700; font-size: 22px; color: var(--ink); }
  .brand__square { width: 18px; height: 18px; background: var(--ink); }
  .brand__circle { width: 44px; height: 44px; border-radius: 50%; background: var(--red); }

  .intro {
    position: absolute; left: 0; right: 0; top: 366px;
    text-align: center; font-weight: 700; font-size: 17.5px; line-height: 27px;
  }
  .features { position: absolute; left: 50px; top: 458px; list-style: none; }
  .features li {
    display: flex; align-items: center; gap: 9px;
    font-size: 17.5px; height: 30.5px;
  }
  .tick { width: 19px; height: 19px; flex: none; }

  .imprint {
    position: absolute; left: 0; right: 0; top: 900px;
    text-align: center; font-size: 14.5px; line-height: 24px;
  }
  .imprint strong { font-weight: 700; }

  .footer {
    position: absolute; left: 0; right: 0; bottom: 0; height: 45px;
    background: var(--footer); color: #fff;
    display: flex; align-items: center; justify-content: center; font-size: 15px;
  }
</style>
</head>
<body>

<section class="flyer flyer--front">
  <div class="photo" role="img" aria-label="Foto: lächelnder Handwerker in roter Kappe und blauer Latzhose mit verschränkten Armen in heller Küche"></div>
  <svg class="wave" viewBox="0 0 504 60" preserveAspectRatio="none" aria-hidden="true">
    <path d="M0 60 L0 26 Q252 -14 504 22 L504 60 Z" fill="var(--red)"/>
    <path d="M0 60 L0 48 Q252 14 504 42 L504 60 Z" fill="var(--paper)"/>
  </svg>
  <h1 class="headline">Wir vermieten <span class="accent">möblierte<br>Monteurzimmer</span> auf Zeit.</h1>
  <p class="lead">Sie sind auf der Suche nach einer günstigen<br>und komfortablen Unterkunft für Ihre Mitarbeiter?<br>Dann sind Sie bei uns genau richtig!</p>
  <div class="cta">BUCHEN Sie JETZT SCHNELL und<br>EINFACH: 01629 581706</div>
  <div class="brands">
    <div class="brand"><span class="brand__square"></span>QT Dwelling</div>
    <div class="brand">RuhOrt17<span class="brand__circle"></span></div>
  </div>
  <div class="footer">www.qt-dwelling.de</div>
</section>

<section class="flyer flyer--back">
  <div class="photo" role="img" aria-label="Foto: modernes Wohnzimmer mit hellem Sofa, Pflanze, Bilderrahmen und Hängelampe"></div>
  <svg class="wave" viewBox="0 0 504 60" preserveAspectRatio="none" aria-hidden="true">
    <path d="M0 60 L0 20 Q252 -12 504 14 L504 60 Z" fill="var(--red)"/>
    <path d="M0 60 L0 48 Q252 12 504 40 L504 60 Z" fill="var(--paper)"/>
  </svg>
  <p class="intro">Überzeugen Sie sich selbst von unserem<br>Angebot &amp; buchen Sie noch heute eines unserer<br>Monteurzimmer! <span class="accent">Wir freuen uns auf Ihren Besuch!</span></p>
  <ul class="features">
    <li><svg class="tick" viewBox="0 0 20 20"><circle cx="9" cy="11" r="7.5" fill="none" stroke="var(--ink)" stroke-width="1.8"/><path d="M5 10.5 L9 14 L18 3" fill="none" stroke="var(--red)" stroke-width="2.4" stroke-linecap="round" stroke-linejoin="round"/></svg>Moderne und komfortable Wohnungen</li>
    <li><svg class="tick" viewBox="0 0 20 20"><circle cx="9" cy="11" r="7.5" fill="none" stroke="var(--ink)" stroke-width="1.8"/><path d="M5 10.5 L9 14 L18 3" fill="none" stroke="var(--red)" stroke-width="2.4" stroke-linecap="round" stroke-linejoin="round"/></svg>TV und Kühlschränke auf jedem Zimmer</li>
    <li><svg class="tick" viewBox="0 0 20 20"><circle cx="9" cy="11" r="7.5" fill="none" stroke="var(--ink)" stroke-width="1.8"/><path d="M5 10.5 L9 14 L18 3" fill="none" stroke="var(--red)" stroke-width="2.4" stroke-linecap="round" stroke-linejoin="round"/></svg>Voll ausgestattete Küche</li>
    <li><svg class="tick" viewBox="0 0 20 20"><circle cx="9" cy="11" r="7.5" fill="none" stroke="var(--ink)" stroke-width="1.8"/><path d="M5 10.5 L9 14 L18 3" fill="none" stroke="var(--red)" stroke-width="2.4" stroke-linecap="round" stroke-linejoin="round"/></svg>Immer mit Balkon oder Terrasse</li>
    <li><svg class="tick" viewBox="0 0 20 20"><circle cx="9" cy="11" r="7.5" fill="none" stroke="var(--ink)" stroke-width="1.8"/><path d="M5 10.5 L9 14 L18 3" fill="none" stroke="var(--red)" stroke-width="2.4" stroke-linecap="round" stroke-linejoin="round"/></svg>Kostenloses schnelles W-Lan</li>
    <li><svg class="tick" viewBox="0 0 20 20"><circle cx="9" cy="11" r="7.5" fill="none" stroke="var(--ink)" stroke-width="1.8"/><path d="M5 10.5 L9 14 L18 3" fill="none" stroke="var(--red)" stroke-width="2.4" stroke-linecap="round" stroke-linejoin="round"/></svg>Gute Parkmöglichkeiten</li>
    <li><svg class="tick" viewBox="0 0 20 20"><circle cx="9" cy="11" r="7.5" fill="none" stroke="var(--ink)" stroke-width="1.8"/><path d="M5 10.5 L9 14 L18 3" fill="none" stroke="var(--red)" stroke-width="2.4" stroke-linecap="round" stroke-linejoin="round"/></svg>Willkommenspaket</li>
  </ul>
  <div class="cta">BUCHEN Sie JETZT SCHNELL und<br>EINFACH: 01629 581706</div>
  <div class="brands">
    <div class="brand"><span class="brand__square"></span>QT Dwelling</div>
    <div class="brand">RuhOrt17<span class="brand__circle"></span></div>
  </div>
  <p class="imprint"><strong>Kranzhof Co-living GmbH</strong> • Lindenbogen 14 • 10245 Berlin<br>Tel.: +49 40 613870255 • E-Mail: info@qt-dwelling.de</p>
  <div class="footer">www.qt-dwelling.de</div>
</section>

</body>
</html>
```